Business card

We need a business card design for our company based in Auckland , New Zealand called 'Kestrel + Design Ltd'. We provide architectural services. We would like to see designs that use the max. three colours (such as white, black, grey) The final design should communicate financial safety and growth."
Also I will provide our company logo. I would like to the logo to be embeded onto our business card.

Target Market(s)

new residential house, alteration & addition & light commericila design & drafting service

Industry/Entity Type

Architecture

Contact Information for Business Card

Company name: kestrel + design Ltd.
Name: Mark Telford
Job title: architectural designer & Design RQC
email address: mark@kdstudio.co.nz
mobile number: 02 5319 6620
web site: www.kdstudio.co.nz

Requirements
Must have
• My project must have..
• - embeded logo (attached company logo)
• I don't have a bigger version for our company logo, but I have one old one, so you can remove the word from it)
• - insert the attached small PDGQ logo & RQC logo
• - creative, simple and clear business card.
• - Max. three colours
Nice to have
• - Here are the samples I would like to share with you: http://www.velmorindex.com/blog/minimalistic-business-card-designs/
• I would like to have my business card like one of the creation.
Should not have
• TBA

```html
<!DOCTYPE html>
<html lang="en">
<head>
<meta charset="utf-8">
<title>Kestrel + Design Ltd – Business Card</title>
<link rel="stylesheet" href="https://fonts.googleapis.com/css2?family=Oswald:wght@300;400;600&display=swap">
<style>
  :root {
    --ink: #0b0b0b;
    --paper: #ffffff;
    --grey: #8a8a8a;
    --grey-light: #b9b9b9;
    --stage: #d9d9d9;
  }
  * { box-sizing: border-box; margin: 0; padding: 0; }
  html, body {
    width: 1200px; height: 900px; overflow: hidden;
    background: var(--stage);
    font-family: "Oswald", "Arial Narrow", sans-serif;
  }
  .sheet {
    width: 1200px; height: 900px;
    display: flex; flex-direction: column; align-items: center; justify-content: center;
    gap: 40px;
  }
  .card {
    position: relative;
    width: 630px; height: 360px;
    box-shadow: 0 6px 18px rgba(0,0,0,.18);
  }

  /* Front */
  .card--front {
    background: var(--ink); color: var(--paper);
    display: flex; flex-direction: column; align-items: center; justify-content: center;
    gap: 26px;
  }
  .front-ring {
    width: 120px; height: 120px; border-radius: 50%;
    border: 3px solid var(--paper);
  }
  .front-name {
    font-weight: 300; font-size: 24px; letter-spacing: .5px;
  }

  /* Back */
  .card--back { background: var(--paper); color: var(--ink); }
  .badges {
    position: absolute; top: 30px; right: 40px;
    display: flex; gap: 18px; align-items: center;
  }
  .badge-round {
    width: 62px; height: 62px; border-radius: 50%;
    background: var(--ink);
  }
  .badge-block {
    width: 74px; height: 62px;
    background: var(--grey);
  }
  .rule-top {
    position: absolute; top: 108px; left: 390px; right: 0;
    height: 1px; background: var(--grey);
  }
  .heading-row {
    position: absolute; top: 130px; left: 40px; right: 210px;
    display: flex; align-items: center; gap: 14px;
  }
  .heading-row .company {
    font-weight: 300; font-size: 22px; white-space: nowrap;
  }
  .heading-row .rule {
    flex: 1; height: 2px; background: var(--grey);
  }
  .contact {
    position: absolute; left: 40px; top: 190px;
  }
  .contact .mark-row {
    display: flex; align-items: center; gap: 10px;
    font-weight: 300; font-size: 18px; margin-bottom: 12px;
  }
  .contact .mark-dot {
    width: 30px; height: 30px; border-radius: 50%;
    border: 2px solid var(--ink);
  }
  .person { font-weight: 600; font-size: 21px; line-height: 1.1; }
  .role { font-weight: 300; font-size: 15px; color: var(--grey); margin-bottom: 6px; }
  .line { font-weight: 300; font-size: 15px; line-height: 1.35; }
  .line--web { font-weight: 400; }
</style>
</head>
<body>
  <main class="sheet">
    <section class="card card--front" aria-label="Business card front">
      <div class="front-ring" aria-hidden="true"></div>
      <p class="front-name">Kestrel + Design Ltd.</p>
    </section>

    <section class="card card--back" aria-label="Business card back">
      <div class="badges">
        <div class="badge-round" role="img" aria-label="Licensed practitioner badge"></div>
        <div class="badge-block" role="img" aria-label="PDGQ professional member badge"></div>
      </div>
      <div class="rule-top"></div>

      <div class="heading-row">
        <span class="company">kestrel + design Ltd.</span>
        <span class="rule"></span>
      </div>

      <div class="contact">
        <div class="mark-row">
          <span class="mark-dot" aria-hidden="true"></span>
          <span>kestrel + design Ltd.</span>
        </div>
        <p class="person">Mark Telford</p>
        <p class="role">Architectural designer &amp; Design RQC</p>
        <p class="line">02 5319 6620</p>
        <p class="line">mark@kdstudio.co.nz</p>
        <p class="line line--web">www.kdstudio.co.nz</p>
      </div>
    </section>
  </main>
</body>
</html>
```